Nine Lanterns Quill House Book Cover for: "Growing Older Wisely"

We are a publishing company who plans to launch the book, Growing Older Wisely, A Handy Compact Manual for Legal, Financial and Emotional Health in late 2018. We desire a book cover that creates interest, looks professional and can draw readers to open and purchase this book. Growing Older Wisely is an invaluable, self-help book which provides Generation X, Baby Boomers and their families with the following information: steps to obtain valid, reliable wills and trusts, identify and pay for health care, address end of life care and manage grief. (Please see the attached book description for more information about the book contents). The cover needs to have a "wellness", health and healing emphasis but it should not be morbid. Instead, the cover should have an uplifting, inviting and engaging feeling.

The designer should use Photoshop to develop the 5 x 7 cover. Please design the front, back cover and spine using the attached suggested layout as a guide. Use colors that complement the background colors in the author's photo and the logo for the front and back colors. Feel free to change the colors of the black rectangles on the front of the book. We are looking for a design to be added using the suggested layouts but we are open to modifications of the layout provided that all the content in the attachments are used. Below are the specifications needed for the cover:

-Use Photoshop
-Develop a front and back cover for a 5 x 7 format book
-Include the book title, subtitle and author name on the front cover as noted on the front cover attachment
-Include a book title and author names on the spine of the cover
-Use full bleed background if appropriate
-Color correct and resize images as necessary
-Insert logo and publisher’s imprint on spine and back cover as noted in attachments

For designers who are successful with this contest, we will primarily consider you for future projects.

Thanks!

Target Market(s)

Generation X, Baby Boomers and their families

Industry/Entity Type

Book Publisher

Font styles to use
Sans Serif

Colors

Designer to choose colors to be used in the design.

Requirements
Must have
• The designer should use Photoshop to develop the 5 x 7 cover. Please design the front, back cover and spine using the attached suggested layout as a guide. Use colors that complement the background colors in the author's photo and the logo for the front and back colors. Feel free to change the colors of the black rectangles on the front of the book. We are looking for a design to be added using the suggested layouts but we are open to modifications of the layout provided that all the content in the attachments are used. Below are the specifications needed for the cover:
• -Use Photoshop
• -Develop a front and back cover for a 5 x 7 format book
• -Include the book title, subtitle and author name on the front cover as noted on the front cover attachment
• -Include a book title and author names on the spine of the cover
• -Use full bleed background if appropriate
• -Color correct and resize images as necessary
• -Insert logo and publisher’s imprint on spine and back cover as noted in attachments
Nice to have
• N/A
Should not have
• The design should not specifically duplicate the layout samples or include pictures of persons on the cover. We have provided those as a guide; we are looking for innovation and professionalism.

```html
<!DOCTYPE html>
<html lang="en">
<head>
<meta charset="utf-8">
<title>Growing Older Wisely – Cover</title>
<link rel="stylesheet" href="https://fonts.googleapis.com/css2?family=Oswald:wght@400;500&family=Roboto:wght@400&family=Roboto+Condensed:wght@400&display=swap">
<style>
  :root {
    --page-bg: #ececec;
    --cover-navy: #1d2430;
    --cover-navy-deep: #151b24;
    --accent-orange: #f3976c;
    --text-light: #f4f4f4;
    --teal: #4fa3b8;
    --glow-orange: #e0783f;
    --photo-green: #5d6e4a;
    --photo-navy: #27304a;
  }
  * { box-sizing: border-box; margin: 0; padding: 0; }
  html, body { width: 1200px; height: 800px; overflow: hidden; }
  body {
    background: radial-gradient(ellipse at center, #f7f7f7 0%, var(--page-bg) 80%);
    font-family: "Roboto Condensed", "Arial Narrow", sans-serif;
    color: var(--text-light);
  }
  .cover-spread {
    position: absolute;
    left: 137px; top: 90px;
    width: 926px; height: 620px;
    display: flex;
    box-shadow: 0 14px 40px rgba(0,0,0,0.25);
  }
  .front-cover, .back-cover {
    position: relative;
    width: 443px; height: 620px;
    background: var(--cover-navy);
    overflow: hidden;
  }

  /* Spine */
  .spine {
    width: 40px; height: 620px;
    background: var(--cover-navy-deep);
    border-left: 1px solid rgba(255,255,255,0.06);
    border-right: 1px solid rgba(255,255,255,0.06);
    display: flex; flex-direction: column; align-items: center;
    justify-content: space-between;
    padding: 28px 0 24px;
    overflow: hidden;
  }
  .spine-text {
    writing-mode: vertical-rl;
    white-space: nowrap;
    display: flex; align-items: center; gap: 22px;
  }
  .spine-title {
    font-family: "Oswald", sans-serif;
    font-size: 15px; letter-spacing: 1px;
    color: var(--accent-orange);
  }
  .spine-authors { font-size: 11px; color: var(--text-light); }
  .spine-publisher {
    writing-mode: vertical-rl;
    white-space: nowrap;
    display: flex; align-items: center; gap: 8px;
    font-size: 10px; color: var(--text-light);
  }
  .spine-publisher .mark-square {
    width: 12px; height: 12px; background: var(--accent-orange);
  }

  /* Front */
  .front-title {
    position: absolute; top: 44px; left: 0; right: 0;
    text-align: center;
    font-family: "Oswald", sans-serif; font-weight: 400;
    font-size: 42px; letter-spacing: 0.5px;
    color: var(--accent-orange);
  }
  .front-subtitle {
    position: absolute; top: 112px; left: 0; right: 0;
    text-align: center;
    font-family: "Roboto", sans-serif;
    font-size: 16px; line-height: 1.25;
    color: var(--text-light);
  }
  .front-artwork {
    position: absolute; left: 0; right: 0; top: 170px; bottom: 0;
    background:
      radial-gradient(ellipse 45% 30% at 40% 25%, rgba(79,163,184,0.75), transparent 70%),
      radial-gradient(ellipse 40% 25% at 55% 45%, rgba(224,120,63,0.7), transparent 70%),
      radial-gradient(ellipse 60% 35% at 50% 80%, rgba(140,160,185,0.45), transparent 75%),
      linear-gradient(180deg, var(--cover-navy) 0%, #27384a 35%, #3a3f4a 65%, #2a3240 100%);
  }
  .front-authors {
    position: absolute; left: 0; right: 0; bottom: 28px;
    text-align: center;
    font-family: "Roboto", sans-serif;
    color: var(--text-light);
  }
  .front-authors .lead-author {
    display: block;
    font-family: "Oswald", sans-serif;
    font-size: 20px; letter-spacing: 1px;
    color: var(--accent-orange);
  }
  .front-authors .contributor { font-size: 13px; }

  /* Back */
  .back-blurb {
    position: absolute; top: 30px; left: 24px; right: 26px;
    font-size: 12px; line-height: 1.36;
    text-align: justify;
  }
  .back-blurb p { margin-bottom: 8px; }
  .author-photo {
    position: absolute; left: 24px; top: 300px;
    width: 104px; height: 136px;
    background: linear-gradient(180deg, var(--photo-green) 0%, #7b8a5e 45%, var(--photo-navy) 100%);
  }
  .author-bio {
    position: absolute; left: 142px; right: 26px; top: 296px;
    font-size: 12px; line-height: 1.36; text-align: justify;
  }
  .imprint {
    position: absolute; left: 24px; top: 515px;
    font-size: 11px; line-height: 1.4;
  }
  .publisher-mark {
    position: absolute; left: 24px; bottom: 54px;
    display: flex; align-items: center; gap: 8px;
    font-size: 11px;
  }
  .publisher-mark .mark-square {
    width: 16px; height: 16px; background: var(--accent-orange);
  }
  .isbn-block {
    position: absolute; right: 26px; bottom: 48px;
    font-size: 11.5px; line-height: 1.4;
  }
</style>
</head>
<body>
  <main class="cover-spread">
    <section class="back-cover">
      <div class="back-blurb">
        <p>Death and taxes may be inevitable, but they both require a lot of preparation. Fifty percent of America’s seventy-four million baby boomers have parents eighty or older, and nearly half of those boomers haven’t discussed end-of-life issues with their loved ones.</p>
        <p>In Growing Older Wisely, the authors present a detailed, step-by-step guide on how to deal with aging. They tackle issues such as wills and trusts, estate planning, senior housing, caregiving, hospice care, and death and bereavement. Their approach is lighthearted but thorough, and they provide a sorely needed examination of all the details involved in growing old in America.</p>
        <p>Dana R. Whitfield is a social services administrator, and Contributor Martin E. Holloway is an attorney. They have combined their skills and knowledge to give readers a practical understanding of the issues involved in caring for an elderly family member.</p>
      </div>
      <div class="author-photo" role="img" aria-label="Portrait photo of the author"></div>
      <p class="author-bio">Dana R. Whitfield holds an advanced degree in Public Administration from Eastbrook State University and is currently an Administrator at the Westmoor County Office of Social Services. Collaborator Martin E. Holloway is an attorney who has practiced for thirty-five years in the areas of family law, wills, trusts, and estate planning. In Growing Older Wisely, the two have pooled their expertise to provide an invaluable guide to all the issues involved in caring for a loved one at the end of his or her life.</p>
      <p class="imprint">NINE LANTERNS QUILL HOUSE<br>Published in paperback and ebook</p>
      <div class="publisher-mark"><span class="mark-square"></span><span>Nine Lanterns Quill House</span></div>
      <p class="isbn-block">978-0-000-41825-3 (paperback)<br>ISBN: 978-0-000-41826-0 (ebook)</p>
    </section>

    <aside class="spine">
      <div class="spine-text">
        <span class="spine-title">GROWING OLDER WISELY</span>
        <span class="spine-authors">Dana R. Whitfield · Martin E. Holloway</span>
      </div>
      <div class="spine-publisher"><span class="mark-square"></span><span>Nine Lanterns Quill House</span></div>
    </aside>

    <section class="front-cover">
      <div class="front-artwork" role="img" aria-label="Illustration of a glowing world map over financial charts and stacks of coins"></div>
      <h1 class="front-title">GROWING OLDER WISELY</h1>
      <p class="front-subtitle">A Handy Compact Manual<br>for Legal, Financial and Emotional Health</p>
      <p class="front-authors"><span class="lead-author">DANA R. WHITFIELD</span><span class="contributor">with Martin E. Holloway</span></p>
    </section>
  </main>
</body>
</html>
```